Frostwyn.co - Polar Expeditions Specialists

We need a modern, visually striking business card for Frostwyn.co, a company specialized in selling expedition cruises to the most remote regions on Earth, with a focus on the Arctic and Antarctica. The design should instantly communicate that the cardholder is an expert in polar travel. Use clean, premium aesthetics with cool tones like icy blue and white, possibly incorporating polar imagery (ice, glaciers, penguins, etc.)

Attached the logo

Contact Information for Business Card

Feels high-end and trustworthy.. Visually memorable — encourages people to keep it

Colors
0054AA
0677BA
7BADD7
CADEEF
E8F1F8

Requirements
Must have
• ice, glaciers, penguins, montains
Nice to have
• modern, transparente,

```html
<!DOCTYPE html>
<html lang="en">
<head>
<meta charset="UTF-8">
<title>Frostwyn.co – Business Card</title>
<link href="https://fonts.googleapis.com/css2?family=Poppins:wght@600;700&family=Lato:wght@400;700&display=swap" rel="stylesheet">
<style>
  :root {
    --ink: #1e4f96;
    --ink-deep: #0054AA;
    --blue-mid: #0677BA;
    --blue-soft: #7BADD7;
    --ice: #CADEEF;
    --frost: #E8F1F8;
    --card: #f2f4f7;
    --backdrop: #e6e3df;
  }
  * { box-sizing: border-box; margin: 0; padding: 0; }
  html, body {
    width: 1200px; height: 900px; overflow: hidden;
    background: var(--backdrop);
  }
  .stage { position: relative; width: 1200px; height: 900px; }
  .card {
    position: absolute; left: 280px; top: 236px;
    width: 672px; height: 385px;
    background: var(--card);
    border-radius: 14px;
    box-shadow: 0 2px 10px rgba(40, 50, 70, 0.12);
    overflow: hidden;
  }
  .polar-art {
    position: absolute; left: 40px; top: 30px;
    width: 295px; height: 355px;
    border-radius: 120px 120px 0 0;
    background:
      radial-gradient(ellipse at 40% 35%, var(--blue-soft) 0%, transparent 60%),
      linear-gradient(160deg, var(--blue-mid) 0%, var(--ink-deep) 70%, var(--ink) 100%);
    opacity: 0.85;
  }
  .brand {
    position: absolute; left: 383px; top: 36px;
    font-family: "Poppins", sans-serif;
    color: var(--ink);
  }
  .brand-name {
    font-weight: 700; font-size: 42px; line-height: 1; white-space: nowrap;
  }
  .brand-tagline {
    font-weight: 600; font-size: 14.5px; margin-top: 8px; white-space: nowrap;
  }
  .holder {
    position: absolute; left: 383px; top: 134px;
    font-family: "Lato", sans-serif; color: var(--ink);
  }
  .holder-name {
    font-weight: 700; font-size: 25px; letter-spacing: 0.4px; line-height: 1;
  }
  .holder-role { font-size: 16px; margin-top: 6px; }
  .contacts {
    position: absolute; left: 383px; top: 205px;
    list-style: none;
    font-family: "Lato", sans-serif; font-size: 14px; letter-spacing: 0.7px;
    color: var(--ink);
  }
  .contacts li {
    display: flex; align-items: flex-start; gap: 12px;
    line-height: 24.5px; white-space: nowrap;
  }
  .contacts .icon {
    width: 13px; height: 13px; margin-top: 6px; flex: none;
    fill: var(--ink);
  }
</style>
</head>
<body>
<main class="stage">
  <article class="card">
    <div class="polar-art" role="img" aria-label="Blue silhouette illustration of a polar bear with two penguins and small stars"></div>

    <header class="brand">
      <h1 class="brand-name">Frostwyn.co</h1>
      <p class="brand-tagline">Polar Expeditions Specialists</p>
    </header>

    <section class="holder">
      <h2 class="holder-name">DANIEL HARROW</h2>
      <p class="holder-role">Founder &amp; CEO</p>
    </section>

    <ul class="contacts">
      <li>
        <svg class="icon" viewBox="0 0 14 14"><path d="M7 0.5a4.6 4.6 0 0 0-4.6 4.6C2.4 8.5 7 13.5 7 13.5s4.6-5 4.6-8.4A4.6 4.6 0 0 0 7 0.5zm0 6.4a1.8 1.8 0 1 1 0-3.6 1.8 1.8 0 0 1 0 3.6z"/></svg>
        <span>418 Glacier Row Suite Two<br>Tromsfield, North, Norland 04712</span>
      </li>
      <li>
        <svg class="icon" viewBox="0 0 14 14"><path d="M3 1l2.2 2.6-1.2 1.6a8 8 0 0 0 4.8 4.8l1.6-1.2L13 11l-1.4 2C6 13 1 8 1 2.4z"/></svg>
        <span>(355) 218-4402</span>
      </li>
      <li>
        <svg class="icon" viewBox="0 0 14 14"><path d="M4 0.5h6a1 1 0 0 1 1 1v11a1 1 0 0 1-1 1H4a1 1 0 0 1-1-1v-11a1 1 0 0 1 1-1zm0.6 1.6v8.6h4.8V2.1zM7 11.3a0.8 0.8 0 1 0 0 1.6 0.8 0.8 0 0 0 0-1.6z"/></svg>
        <span>(355) 218-4402</span>
      </li>
      <li>
        <svg class="icon" viewBox="0 0 14 14"><path d="M1 3h12v8.5H1zm1.2 1.2v0.3L7 7.6l4.8-3.1v-0.3zm0 1.7v4.4h9.6V5.9L7 9z"/></svg>
        <span>hello@frostwyn.co</span>
      </li>
      <li>
        <svg class="icon" viewBox="0 0 14 14"><path d="M7 0.8a6.2 6.2 0 1 0 0 12.4A6.2 6.2 0 0 0 7 0.8zm-0.6 11c-2.3-0.3-4-2.3-4-4.8 0-0.4 0.1-0.8 0.1-1.1l3 3v0.6c0 0.7 0.6 1.2 1.2 1.2zm4.2-1.6c-0.2-0.5-0.6-0.8-1.1-0.8h-0.6V7.6c0-0.3-0.3-0.6-0.6-0.6H4.7V5.8h1.2c0.3 0 0.6-0.3 0.6-0.6V4h1.2c0.7 0 1.2-0.6 1.2-1.2v-0.3a4.8 4.8 0 0 1 1.7 7.7z"/></svg>
        <span>frostwyn.co</span>
      </li>
    </ul>
  </article>
</main>
</body>
</html>
```